Marvia Quenby Business Cards

We Need two Business Cards with bleeds. the only difference between the two cards is the backaround color one lilac and pink. Attached we have the cards please match up the logo's and text. Take out the orange box out.

Target Market(s)

double-sided business cards

Industry/Entity Type

Business

Logo Text

match up as best as possible

Colors
f59195
d2a4cc

Requirements
Must have
• n/a
Nice to have
• n/a
Should not have
• n/a

```html
<!DOCTYPE html>
<html lang="en">
<head>
<meta charset="utf-8">
<title>Marvia Quenby-Ashford, MD — Business Cards</title>
<link rel="stylesheet" href="https://fonts.googleapis.com/css2?family=Abril+Fatface&family=Cinzel:wght@500;700&family=Cookie&family=Cormorant+SC:wght@500&family=Great+Vibes&family=Montserrat:wght@400;700&family=Old+Standard+TT&family=Yellowtail&display=swap">
<style>
  :root {
    --lilac: #d2a4cc;
    --pink: #f59195;
    --white: #ffffff;
    --bronze: #8a6a2a;
    --gold: #cdb85e;
    --gold-bright: #d9c23a;
    --cocoa: #3a2422;
    --maroon: #8a2c2c;
    --slate: #8a93a8;
    --ink: #2a1c1c;
    --arrow: #c08a3a;
  }
  * { margin: 0; padding: 0; box-sizing: border-box; }
  html, body { width: 1200px; height: 1200px; overflow: hidden; background: var(--white); }
  .sheet { position: relative; width: 1200px; height: 1200px; }
  .card { position: absolute; width: 576px; height: 338px; overflow: hidden; }
  .card--lilac { background: var(--lilac); }
  .card--pink { background: var(--pink); }
  .front-lilac { left: 16px; top: 134px; }
  .front-pink { left: 608px; top: 134px; }
  .back-lilac { left: 16px; top: 726px; }
  .back-pink { left: 608px; top: 726px; }
  .abs { position: absolute; }

  /* Front lilac */
  .frame { left: 24px; top: 30px; width: 530px; height: 188px; border: 2px solid var(--white); border-bottom: none; }
  .frame-base { height: 2px; background: var(--white); top: 216px; }
  .title-name, .title-cert { left: 0; width: 576px; text-align: center; color: var(--white);
    font-family: "Cormorant SC", serif; font-size: 33px; letter-spacing: 1px; line-height: 1; }
  .title-name { top: 96px; }
  .title-cert { top: 136px; }
  .tagline { left: 0; width: 576px; top: 209px; text-align: center; color: var(--white);
    font-family: "Montserrat", sans-serif; font-size: 13px; }
  .mark-area { left: 262px; top: 178px; width: 78px; height: 124px; border-radius: 40% 40% 50% 50%;
    background: radial-gradient(circle, rgba(120,70,70,0.35), rgba(120,70,70,0.1)); }

  /* Front pink */
  .seal-label { left: 0; width: 580px; top: 94px; text-align: center; color: var(--bronze);
    font-family: "Old Standard TT", serif; font-size: 14px; }
  .script-name { left: 120px; top: 144px; width: 420px; color: var(--bronze); font-family: "Yellowtail", cursive;
    font-size: 34px; white-space: nowrap; line-height: 1; }
  .script-name .suffix { font-family: "Great Vibes", cursive; font-size: 28px; }
  .appt-oval { left: 360px; top: 178px; width: 164px; height: 76px; border-radius: 50%; background: var(--gold); opacity: 0.92; }
  .appt-text { left: 360px; top: 190px; width: 164px; text-align: center; color: var(--bronze);
    font-family: "Great Vibes", cursive; font-size: 22px; }
  .specialty { left: 220px; width: 140px; top: 206px; text-align: center; color: var(--bronze);
    font-family: "Old Standard TT", serif; font-size: 14px; line-height: 16px; }

  /* Back lilac */
  .disc { left: 192px; top: 20px; width: 196px; height: 196px; border-radius: 50%; background: var(--white); }
  .services { left: 190px; width: 200px; top: 94px; text-align: center; color: var(--maroon);
    font-family: "Cinzel", serif; font-weight: 700; font-size: 8.5px; line-height: 12.5px; }
  .ribbon-appt { left: 174px; width: 228px; top: 156px; text-align: center; color: var(--maroon);
    font-family: "Great Vibes", cursive; font-size: 27px; line-height: 1; }
  .band-white { left: 0; top: 252px; width: 576px; height: 86px; background: var(--white); }
  .band-under { left: 106px; top: 252px; width: 379px; height: 86px; background: var(--lilac); }
  .contact-band { left: 44px; top: 252px; width: 489px; height: 69px; background: var(--slate);
    color: var(--white); font-family: "Cookie", cursive; font-size: 18px; line-height: 22px; }
  .contact-band .addr { position: absolute; left: 64px; top: 2px; }
  .contact-band .phones { position: absolute; left: 316px; top: 2px; }
  .contact-band .mail { position: absolute; left: 0; width: 489px; top: 46px; text-align: center; }

  /* Back pink */
  .svc-list { left: 12px; top: 0; width: 230px; }
  .svc { position: absolute; left: 0; width: 230px; text-align: center; color: var(--ink);
    font-family: "Cinzel", serif; font-weight: 500; font-size: 21px; line-height: 1; }
  .rule { position: absolute; left: 0; width: 230px; height: 2px; background: #5a4040; }
  .info-box { left: 294px; top: 62px; width: 229px; height: 228px; border-radius: 14px; background: var(--gold); }
  .info-addr { left: 294px; width: 229px; top: 129px; text-align: center; color: var(--ink);
    font-family: "Montserrat", sans-serif; font-weight: 700; font-size: 8.5px; }
  .name-band { left: 300px; top: 160px; width: 218px; height: 61px; background: var(--pink); }
  .name-band-text { left: 300px; top: 160px; width: 218px; height: 61px; text-align: center; color: var(--ink);
    font-family: "Abril Fatface", serif; font-size: 36px; letter-spacing: 5px; line-height: 61px; }
  .info-contact { left: 294px; width: 229px; top: 245px; text-align: center; color: var(--ink);
    font-family: "Montserrat", sans-serif; font-weight: 700; font-size: 11px; line-height: 13px; }
</style>
</head>
<body>
<main class="sheet">

  <section class="card card--lilac front-lilac">
    <div class="abs frame"></div>
    <div class="abs frame-base" style="left:24px;width:100px"></div>
    <div class="abs frame-base" style="left:454px;width:100px"></div>
    <div class="abs title-name">Marvia Quenby-Ashford, MD</div>
    <div class="abs title-cert">Board Certified</div>
    <div class="abs tagline">Women's Health &amp; Wellness Specialist</div>
    <div class="abs mark-area" role="img" aria-label="Mother and child emblem"></div>
  </section>

  <section class="card card--pink front-pink">
    <svg class="abs" style="left:0;top:0" width="576" height="338" viewBox="0 0 576 338">
      <g fill="none" stroke="var(--bronze)" stroke-width="3">
        <path d="M 174 124 A 124 124 0 0 1 406 124"/>
        <path d="M 186 122 A 112 112 0 0 1 394 122"/>
        <path d="M 178 214 A 124 124 0 0 0 402 214"/>
        <path d="M 190 212 A 112 112 0 0 0 390 212"/>
      </g>
      <circle cx="76" cy="242" r="40" fill="var(--cocoa)"/>
      <circle cx="124" cy="240" r="36" fill="#4a302c"/>
      <circle cx="98" cy="272" r="36" fill="var(--gold-bright)" role="img" aria-label="Mother and child emblem"/>
    </svg>
    <div class="abs seal-label">Board Certified</div>
    <div class="abs appt-oval"></div>
    <div class="abs script-name">Marvia Quenby-Ashford <span class="suffix">MD</span></div>
    <div class="abs appt-text">by appointment</div>
    <div class="abs specialty">Women's Health<br>and Wellness<br>Specialist</div>
  </section>

  <section class="card card--lilac back-lilac">
    <svg class="abs" style="left:0;top:0" width="576" height="338" viewBox="0 0 576 338">
      <polygon points="164,158 190,158 190,202 148,202 172,180" fill="var(--white)"/>
      <polygon points="412,158 386,158 386,202 428,202 404,180" fill="var(--white)"/>
    </svg>
    <div class="abs disc"></div>
    <div class="abs" style="left:174px;top:158px;width:228px;height:44px;background:var(--white)"></div>
    <svg class="abs" style="left:0;top:0" width="576" height="338" viewBox="0 0 576 338">
      <rect x="176" y="188" width="30" height="10" rx="4" fill="var(--maroon)"/>
      <rect x="370" y="188" width="30" height="10" rx="4" fill="var(--maroon)"/>
    </svg>
    <div class="abs services">Obstetrics<br>Gynaecology<br>Family Planning<br>Weight Management<br>Menopause</div>
    <div class="abs ribbon-appt">by appointment</div>
    <div class="abs band-white"></div>
    <div class="abs band-under"></div>
    <svg class="abs" style="left:0;top:294px" width="576" height="22" viewBox="0 0 576 22">
      <polygon points="0,2 8,11 0,20" fill="var(--lilac)"/>
      <polygon points="576,2 568,11 576,20" fill="var(--lilac)"/>
    </svg>
    <div class="abs contact-band">
      <div class="addr">48-20 Brookfield Parkway<br>Westbrook, New York 11415</div>
      <div class="phones">(PH) 718.555.0142<br>(FX) 718.555.0143</div>
      <div class="mail">E-mail mq-ashford@mailnest.net</div>
    </div>
  </section>

  <section class="card card--pink back-pink">
    <svg class="abs" style="left:0;top:0" width="576" height="60" viewBox="0 0 576 60">
      <g fill="none" stroke="var(--arrow)" stroke-width="3" stroke-linejoin="round">
        <line x1="14" y1="28" x2="240" y2="28"/>
        <polyline points="14,16 26,28 14,40"/>
        <polyline points="28,16 40,28 28,40"/>
        <polyline points="42,16 54,28 42,40"/>
        <polyline points="226,14 240,28 226,42"/>
      </g>
    </svg>
    <div class="abs svc-list">
      <div class="rule" style="top:62px"></div>
      <div class="svc" style="top:78px">Obstetrics</div>
      <div class="rule" style="top:114px"></div>
      <div class="rule" style="top:134px"></div>
      <div class="svc" style="top:149px">Gynecology</div>
      <div class="rule" style="top:186px"></div>
      <div class="rule" style="top:198px"></div>
      <div class="svc" style="top:215px">Family Planning</div>
      <div class="rule" style="top:250px"></div>
      <div class="rule" style="top:272px"></div>
      <div class="svc" style="top:289px">Menopause</div>
      <div class="rule" style="top:324px"></div>
    </div>
    <div class="abs info-box"></div>
    <div class="abs info-addr">360 Harbor Road, Brierton, NY 11090</div>
    <div class="abs name-band"></div>
    <div class="abs name-band-text">HAVEN</div>
    <div class="abs info-contact">PH 516.555.0118/0119<br>FX 516.555.0120<br>mq-ashford@mailnest.net</div>
  </section>

</main>
</body>
</html>
```